International travel site frontpage redesign

We sell tours to Scandinavia through our website www.velmora-journeys.com. The website has become a bit old fashioned and we are in the process of making the website responsive. As you can see from the attached pictures the website will be wider with the responsive design, and our current design does not fit anymore.

Here is what we are looking for:
- A website that reflects a trustworthy and quality oriented company.
- Making the website more modern looking, but still recognisable (we want to keep the colours).
- keeping in mind that the age group of our customers are from 20-80 years old (most in their 60s).
- We want to remove the popular tours part and are instead looking to replace this with picture boxes the following subjects Scandinavia Specialist, Special Offers, Contact, Norway (or Norway Tours), Sweden (or Sweden Tours), Iceland (or Iceland Tours), Combination Tours. Possibly also Lapland, Winter, Northern Lights, Fjords and Capitals. Some of these categories can be smaller or perhaps half boxes; i.e. Winter and Northern lights in one. If we end up with four boxes per line perhaps we could add a social media box next to the three first ones.
- The above means that the left hand meny with Norway Tours, Sweden Tours etc will be redundant.
- we will add another line to the search Box (on the top): Destinations
- The top menu will have the same categories, but we need to add languages as the website will be in English and German.
- The footer must be changed
- We can take away the box to the right where it says "your window to booking the best of our world"

Reason: One of the decission makers had to go away on business last minute.

Target Market(s)

Travelling to Scandinavia is not low cost, so the website needs to appeal to those that can afford to travel to our destination.
The age group of our customers are from 20-80 years old (most in their 60s).

Industry/Entity Type

Travel

Number of Pages Required

1 page

Requirements
Should not have
• Flashy or cheap looking special offers...

```html
<!DOCTYPE html>
<html lang="en">
<head>
<meta charset="utf-8">
<title>Velmora Journeys – Scandinavia Tours</title>
<link href="https://fonts.googleapis.com/css2?family=Open+Sans:wght@400;600;700&family=Dancing+Script:wght@500;700&display=swap" rel="stylesheet">
<style>
:root{
  --brand-red:#7c0d0f;
  --text-dark:#3a3a3a;
  --text-mid:#666;
  --nav-text:#555;
  --footer-bg:#2c7290;
  --footer-bottom:#245f78;
  --footer-text:#e6f1f5;
  --social-blue:#324e8f;
  --white:#fff;
  --caption-bg:rgba(10,10,10,.82);
}
*{box-sizing:border-box;margin:0;padding:0}
html,body{width:1200px;height:2211px;overflow:hidden}
body{position:relative;font-family:"Open Sans",Arial,sans-serif;background:var(--white);color:var(--text-dark)}

/* header */
.site-header{position:absolute;left:0;top:0;width:1200px;height:95px;background:var(--white)}
.brand{position:absolute;left:100px;top:44px;display:flex;align-items:center;gap:10px;font-size:22px;letter-spacing:1px;color:var(--brand-red);font-weight:400;text-transform:uppercase}
.brand-dot{width:14px;height:14px;background:var(--brand-red);border-radius:50%}
.lang-select{position:absolute;left:777px;top:18px;width:100px;height:25px;border:1px solid #ddd;font-size:11px;color:#999;display:flex;align-items:center;padding-left:8px;gap:6px}
.lang-select .flag{width:14px;height:9px;background:#2b3f83}
.lang-select .caret{margin-left:auto;margin-right:8px;width:0;height:0;border-left:4px solid transparent;border-right:4px solid transparent;border-top:5px solid #aaa}
.search{position:absolute;left:890px;top:18px;width:210px;height:25px;border:1px solid #ddd;font-size:11px;color:#aaa;display:flex;align-items:center;padding-left:10px}
.search svg{position:absolute;right:8px;top:6px}
.main-nav{position:absolute;top:62px;left:0;width:1200px;font-size:13px;color:var(--nav-text)}
.main-nav span{position:absolute;transform:translateX(-50%)}

/* hero */
.hero{position:absolute;left:0;top:95px;width:1200px;height:504px;background:linear-gradient(135deg,#3f7f86 0%,#2d6670 35%,#c8582a 55%,#4a8590 75%,#6a9aa0 100%)}
.hero-title{position:absolute;left:685px;top:200px;color:var(--white);font-family:"Dancing Script",cursive;font-size:36px;font-weight:500;line-height:1;white-space:nowrap}
.hero-sub{position:absolute;left:687px;top:252px;color:var(--white);font-family:"Dancing Script",cursive;font-size:26px;font-weight:500;line-height:1;white-space:nowrap}
.btn{display:inline-flex;align-items:center;justify-content:center;background:var(--brand-red);color:var(--white);font-weight:700;font-size:14px;text-transform:uppercase;border-radius:2px}
.hero .btn{position:absolute;left:688px;top:316px;width:152px;height:44px}

/* sections */
.section-title{position:absolute;left:0;width:1200px;text-align:center;font-size:21px;font-weight:700;color:var(--text-dark);text-transform:uppercase}
.title-rule{position:absolute;height:2px;background:#555}
.welcome-text{position:absolute;left:120px;top:706px;width:960px;text-align:center;font-size:12px;line-height:25px;color:var(--text-mid)}

/* tiles */
.tile{position:absolute;width:187px;height:188px;overflow:hidden}
.tile-photo{position:absolute;inset:0}
.tile-caption{position:absolute;left:0;bottom:0;width:100%;height:36px;background:var(--caption-bg);color:var(--white);font-size:12px;text-transform:uppercase;display:flex;align-items:center;padding:0 15px;white-space:nowrap}
.tile-caption svg{margin-left:auto;flex:none}
.social-tile{background:var(--social-blue);color:var(--white);text-align:center}
.social-tile .name{font-size:30px;font-weight:700;margin-top:16px}
.social-tile .join{font-size:19px;font-weight:700;margin-top:2px}
.social-tile .likes{font-size:17px;margin-top:12px}

/* join banner */
.join-banner{position:absolute;left:0;top:1377px;width:1200px;height:348px;background:linear-gradient(180deg,#3e8aa0 0%,#5aa2b3 40%,#c9b07a 80%,#d8bf86 100%)}
.join-copy{position:absolute;left:150px;top:72px;color:var(--white)}
.join-kicker{font-family:"Dancing Script",cursive;font-size:30px;line-height:1}
.join-title{font-family:"Dancing Script",cursive;font-size:42px;line-height:1.1}
.join-text{width:385px;font-size:12px;line-height:22px;margin-top:6px}
.join-banner .btn{position:absolute;left:150px;top:239px;width:133px;height:42px;font-size:14px}

/* footer */
.site-footer{position:absolute;left:0;top:1725px;width:1200px;height:436px;background:var(--footer-bg);color:var(--footer-text)}
.footer-heading{position:absolute;font-size:12px;font-weight:700;color:var(--white);text-transform:uppercase;white-space:nowrap}
.footer-heading::after{content:"";position:absolute;left:0;top:22px;width:var(--rule,118px);height:1px;background:rgba(255,255,255,.8)}
.footer-links{position:absolute;list-style:none;font-size:10.5px;line-height:22.1px;white-space:nowrap}
.social{position:absolute;width:28px;height:28px;border-radius:50%;background:var(--white)}
.footer-bottom{position:absolute;left:0;top:2161px;width:1200px;height:50px;background:var(--footer-bottom);color:var(--footer-text);font-size:11px;text-align:center;line-height:46px}
</style>
</head>
<body>

<header class="site-header">
  <div class="brand"><span>Velmora</span><span class="brand-dot"></span><span>Journeys</span></div>
  <div class="lang-select"><span class="flag"></span>English<span class="caret"></span></div>
  <div class="search">Search :
    <svg width="12" height="12" viewBox="0 0 12 12"><circle cx="5" cy="5" r="3.6" fill="none" stroke="#bbb" stroke-width="1.4"/><line x1="7.7" y1="7.7" x2="11" y2="11" stroke="#bbb" stroke-width="1.4"/></svg>
  </div>
  <nav class="main-nav">
    <span style="left:565px">Home</span>
    <span style="left:662px">Fjords</span>
    <span style="left:763px">Capitals</span>
    <span style="left:868px">Cruises</span>
    <span style="left:970px">Winter</span>
    <span style="left:1073px">Pictures</span>
  </nav>
</header>

<section class="hero" role="img" aria-label="Two people paddling an orange kayak on open water, other kayakers behind">
  <div class="hero-title">Breathtaking Adventures</div>
  <div class="hero-sub">Enjoy whitewater rafting during an activity tour!</div>
  <a class="btn">View Details</a>
</section>

<h2 class="section-title" style="top:647px">Welcome to Velmora Journeys</h2>
<div class="title-rule" style="left:476px;top:690px;width:248px"></div>
<p class="welcome-text">Explore Scandinavian city life on one of our Scandinavian capitals' tours and city breaks. Each city has its own unique characteristics; Sweden's capital Stockholm - famous for its archipelago and diverse architecture, Denmark's capital Copenhagen - a pulsating metropol and historical oasis, Norway's capital Oslo - combining vibrant city life with the beautiful outdoors. Welcome to the capitals of Scandinavia!</p>

<h2 class="section-title" style="top:827px">Scandinavia Specialist</h2>
<div class="title-rule" style="left:497px;top:870px;width:206px"></div>

<div class="tile" style="left:186px;top:915px">
  <div class="tile-photo" role="img" aria-label="Large cruise ship under a blue sky" style="background:linear-gradient(180deg,#6f9ac8 0%,#c9d6e3 45%,#f2f2f2 70%,#7d8fa3 100%)"></div>
  <div class="tile-caption">Special Offers<svg width="13" height="13" viewBox="0 0 14 14"><circle cx="7" cy="7" r="7" fill="#fff"/><path d="M4 7h5M7 4.5 9.5 7 7 9.5" stroke="#111" stroke-width="1.8" fill="none"/></svg></div>
</div>
<div class="tile" style="left:400px;top:915px">
  <div class="tile-photo" role="img" aria-label="Steep fjord valley with a waterfall" style="background:linear-gradient(180deg,#dfe4ea 0%,#6c7a72 40%,#33413a 100%)"></div>
  <div class="tile-caption">Norway Tours<svg width="13" height="13" viewBox="0 0 14 14"><circle cx="7" cy="7" r="7" fill="#fff"/><path d="M4 7h5M7 4.5 9.5 7 7 9.5" stroke="#111" stroke-width="1.8" fill="none"/></svg></div>
</div>
<div class="tile" style="left:613px;top:915px">
  <div class="tile-photo" role="img" aria-label="Boat on a river between green cliffs" style="background:linear-gradient(180deg,#8fa58a 0%,#4f6a4c 45%,#3d4f44 100%)"></div>
  <div class="tile-caption">Sweden Tours<svg width="13" height="13" viewBox="0 0 14 14"><circle cx="7" cy="7" r="7" fill="#fff"/><path d="M4 7h5M7 4.5 9.5 7 7 9.5" stroke="#111" stroke-width="1.8" fill="none"/></svg></div>
</div>
<div class="tile" style="left:828px;top:915px">
  <div class="tile-photo" role="img" aria-label="Green sea cliffs under a bright blue sky" style="background:linear-gradient(180deg,#2a64c4 0%,#7fb0e6 45%,#4f8a3a 65%,#1f5e90 100%)"></div>
  <div class="tile-caption">Iceland Tours<svg width="13" height="13" viewBox="0 0 14 14"><circle cx="7" cy="7" r="7" fill="#fff"/><path d="M4 7h5M7 4.5 9.5 7 7 9.5" stroke="#111" stroke-width="1.8" fill="none"/></svg></div>
</div>

<div class="tile" style="left:186px;top:1130px">
  <div class="tile-photo" role="img" aria-label="Colourful hot air balloons in a blue sky" style="background:linear-gradient(180deg,#1e5fc0 0%,#5b93d8 55%,#dbe6f2 100%)"></div>
  <div class="tile-caption">Combination Tours<svg width="13" height="13" viewBox="0 0 14 14"><circle cx="7" cy="7" r="7" fill="#fff"/><path d="M4 7h5M7 4.5 9.5 7 7 9.5" stroke="#111" stroke-width="1.8" fill="none"/></svg></div>
</div>
<div class="tile" style="left:400px;top:1130px">
  <div class="tile-photo" role="img" aria-label="Couple in sun hats looking out over a tropical sea" style="background:linear-gradient(180deg,#2f7fd0 0%,#88b8e4 45%,#c4a878 75%,#e8e4dc 100%)"></div>
  <div class="tile-caption">Winter &amp; Nort Lights<svg width="13" height="13" viewBox="0 0 14 14"><circle cx="7" cy="7" r="7" fill="#fff"/><path d="M4 7h5M7 4.5 9.5 7 7 9.5" stroke="#111" stroke-width="1.8" fill="none"/></svg></div>
</div>
<div class="tile" style="left:613px;top:1130px">
  <div class="tile-photo" role="img" aria-label="Family walking hand in hand on a beach" style="background:linear-gradient(180deg,#6aa7dc 0%,#a9cbe8 45%,#d9cdb2 75%,#e8dcc2 100%)"></div>
  <div class="tile-caption">Fjords &amp; Capitals<svg width="13" height="13" viewBox="0 0 14 14"><circle cx="7" cy="7" r="7" fill="#fff"/><path d="M4 7h5M7 4.5 9.5 7 7 9.5" stroke="#111" stroke-width="1.8" fill="none"/></svg></div>
</div>
<div class="tile social-tile" style="left:828px;top:1130px">
  <div class="name">Community</div>
  <div class="join">JOINED NOW</div>
  <svg width="40" height="40" viewBox="0 0 40 40" style="margin-top:10px"><path d="M6 18h7v18H6zM15 18l8-12c2-1 4 0 4 3l-2 8h9c2 0 3 2 3 4l-3 12c-1 2-2 3-4 3H15z" fill="#cfd8ea"/></svg>
  <div class="likes">1785 LIKES</div>
</div>

<section class="join-banner" role="img" aria-label="Two wooden longtail boats on a turquoise tropical beach beneath a green cliff">
  <div class="join-copy">
    <div class="join-kicker">Join to our</div>
    <div class="join-title">Velmora Journeys</div>
    <p class="join-text">Es simplemente el texto de relleno de las imprentas y archivos de texto. Lorem Ipsum ha sido el texto de relleno estándar de las industrias desde el año 1500</p>
  </div>
  <a class="btn">Join Now</a>
</section>

<footer class="site-footer">
  <div class="footer-heading" style="left:116px;top:35px">Tour Types</div>
  <ul class="footer-links" style="left:116px;top:69px">
    <li>Escorted Coach Tours</li><li>Independent Rail Tours</li><li>Independent Short Breaks</li><li>Partly Escorted Tours</li><li>Scandinavian Cruises</li><li>Self Drive Tours</li>
  </ul>
  <div class="footer-heading" style="left:116px;top:226px">Winter Tour Types</div>
  <ul class="footer-links" style="left:116px;top:260px">
    <li>Norway Winter Tours</li><li>Sweden Winter Tours</li><li>Finland Winter Tours</li><li>Iceland Winter Tours</li>
  </ul>

  <div class="footer-heading" style="left:348px;top:35px;--rule:168px">Recently Updated Tours</div>
  <ul class="footer-links" style="left:348px;top:69px">
    <li>Nordlys Igloo Hotel</li><li>Northern Lights Cruise</li><li>Lapland Winter Adventure</li>
  </ul>
  <div class="footer-heading" style="left:348px;top:160px;--rule:168px">Tour Selections</div>
  <ul class="footer-links" style="left:348px;top:194px">
    <li>Fjord Tours</li><li>Scandinavian Capitals</li><li>Scandinavia Cruise Packages</li><li>Exclusive Tours</li><li>Midnight Sun</li><li>Activity Tours</li><li>Meet the locals</li><li>Northern lights</li><li>Norway Toursv</li>
  </ul>

  <ul class="footer-links" style="left:621px;top:35px">
    <li>Sweden Tours</li><li>Iceland Tours</li><li>Göta Canal Cruises</li><li>Coastal Express Cruises</li>
  </ul>
  <div class="footer-heading" style="left:621px;top:145px;--rule:170px">Recently Added Tours</div>
  <ul class="footer-links" style="left:621px;top:180px">
    <li>Baltic &amp; Russian Explorer</li><li>Iceland Wilderness</li><li>Baltic Classical</li>
  </ul>
  <div class="footer-heading" style="left:621px;top:266px;--rule:170px">Winter Selections</div>
  <ul class="footer-links" style="left:621px;top:299px">
    <li>Norway Winter Cruises</li><li>Ice Hotel Holidays</li><li>Winter Rail Tours</li><li>Lapland Winter Tours</li>
  </ul>

  <ul class="footer-links" style="left:896px;top:35px">
    <li>Winter Weekend Breaks</li><li>Winter Tours Unpolished</li>
  </ul>
  <div class="footer-heading" style="left:896px;top:102px;--rule:170px">Velmora Journeys</div>
  <ul class="footer-links" style="left:896px;top:137px">
    <li>About Velmora Journeys</li><li>Booking and Payment Procedure</li><li>Terms and Conditions</li><li>Frequently Asked Questions (FAQ)</li><li>Travel Experiences</li><li>Photo Credits</li><li>Site Map</li><li>Contact</li>
  </ul>
  <div class="footer-heading" style="left:896px;top:333px;--rule:180px">Follow Us</div>
  <span class="social" style="left:895px;top:379px"></span>
  <span class="social" style="left:934px;top:379px"></span>
  <span class="social" style="left:971px;top:379px"></span>
  <span class="social" style="left:1007px;top:379px"></span>
  <span class="social" style="left:1044px;top:379px"></span>
</footer>
<div class="footer-bottom">© 2015 Velmora Journeys AS. All rights reserved.</div>

</body>
</html>
```